Fundraising Study Day East of England. Lift the January blues!

A flyer to advertise a fundraising event of lectures for dental hygienists and therapists in support of the exemption campaign. Currently dental hygienists and therapists require a prescription to deliver certain treatment or recommend certain toothpastes. If we are successful in the campaign we will be able to treat patients without these restrictions.

Industry/Entity Type

Dental

```html
<!DOCTYPE html>
<html lang="en">
<head>
<meta charset="utf-8">
<title>Fundraising Study Day East of England</title>
<link href="https://fonts.googleapis.com/css2?family=Montserrat:wght@300;400;500;600&display=swap" rel="stylesheet">
<style>
  :root {
    --sky: #a9e1ec;
    --sky-light: #d3f1f6;
    --teal-deep: #04607f;
    --panel: #0f5b7c;
    --title: #0b6a8a;
    --body: #3a4852;
    --orange: #f6a833;
    --white: #ffffff;
  }
  * { margin: 0; padding: 0; box-sizing: border-box; }
  html, body { width: 848px; height: 1200px; overflow: hidden; }
  body { font-family: "Montserrat", sans-serif; background: var(--sky); }
  .flyer { position: relative; width: 848px; height: 1200px; overflow: hidden; }
  .backdrop { position: absolute; inset: 0; }
  .headline {
    position: absolute; left: 53px; top: 50px;
    color: var(--title); font-weight: 500; font-size: 42px; line-height: 53px;
  }
  .headline .small { font-size: 33px; }
  .price {
    position: absolute; left: 596px; top: 50px; width: 200px; text-align: center;
    font-weight: 500; line-height: 50px;
  }
  .price .label { color: var(--white); font-size: 50px; display: block; }
  .price .amount { color: var(--orange); font-size: 47px; font-weight: 600; display: block; }
  .intro {
    position: absolute; left: 53px; top: 248px; width: 754px;
    color: var(--body); font-weight: 300; font-size: 23.2px; line-height: 33.6px;
    text-align: justify;
  }
  .agenda { position: absolute; left: 53px; top: 480px; width: 488px; color: var(--body); }
  .agenda h2 { color: var(--title); font-size: 18px; font-weight: 600; margin-bottom: 8px; }
  .slot { margin-bottom: 10px; }
  .slot .time { font-size: 15px; font-weight: 400; line-height: 20px; }
  .slot p { font-size: 12.4px; font-weight: 400; line-height: 20px; text-align: justify; }
  .slot p + p { margin-top: 10px; }
  .details {
    position: absolute; left: 564px; top: 484px; width: 258px; height: 684px;
    background: var(--panel);
    clip-path: polygon(0 0, 100% 9%, 100% 100%, 0 100%);
  }
  .venue, .date {
    position: absolute; right: 28px; text-align: right; color: var(--white);
    font-size: 24px; font-weight: 400; line-height: 36px;
  }
  .venue { top: 88px; }
  .date { top: 262px; line-height: 33px; }
  .date .hours { font-size: 20px; }
  .ticket-art {
    position: absolute; left: 72px; top: 496px; width: 116px; height: 92px;
  }
  .booking {
    position: absolute; left: 20px; top: 598px; width: 218px; text-align: center;
    color: var(--white); font-size: 10.4px; font-weight: 500; line-height: 14px;
    word-break: break-all;
  }
</style>
</head>
<body>
<main class="flyer">
  <svg class="backdrop" width="848" height="1200" viewBox="0 0 848 1200" aria-hidden="true">
    <defs>
      <linearGradient id="bg-fade" x1="0" y1="0" x2="0" y2="1">
        <stop offset="0" stop-color="#a6e0eb"/>
        <stop offset="1" stop-color="#bfe9f1"/>
      </linearGradient>
    </defs>
    <rect width="848" height="1200" fill="url(#bg-fade)"/>
    <path d="M0 170 C200 120 450 260 848 180 L848 260 C520 330 260 170 0 250 Z" fill="#c8eef4" opacity="0.6"/>
    <path d="M0 300 C260 250 520 360 848 300 L848 380 C560 440 240 330 0 400 Z" fill="#d5f2f7" opacity="0.5"/>
    <path d="M0 440 C240 470 520 420 848 470 L848 1120 C560 1060 240 1140 0 1080 Z" fill="#ffffff" opacity="0.92"/>
    <path d="M0 1080 C260 1130 560 1070 848 1120 L848 1200 L0 1200 Z" fill="#9fdce8"/>
    <path d="M0 1100 C280 1150 520 1090 848 1150" stroke="#ffffff" stroke-width="3" fill="none" opacity="0.6"/>
    <path d="M496 0 L848 0 L848 130 C810 200 720 240 640 236 C570 232 520 200 505 150 C490 100 470 40 496 0 Z" fill="var(--teal-deep)"/>
    <path d="M524 0 C510 50 520 90 540 140 C570 200 640 212 700 206 C760 198 810 170 848 148" stroke="#ffffff" stroke-width="3" stroke-dasharray="14 10" fill="none"/>
  </svg>

  <h1 class="headline">Fundraising <span class="small">Study</span><br>Day East of England.<br>Lift the January blues!</h1>

  <div class="price"><span class="label">COST</span><span class="amount">£101.48</span></div>

  <p class="intro">A fundraising event to support our exemptions project. The day will consist of a series of presentations ranging from the new ECPD to new technologies. The aim, being to enhance our learning and raise funds to support the exemptions campaign. The speaker line includes some of the UK and Irelands most respected dental prefossionals in our field.</p>

  <section class="agenda">
    <h2>Agenda</h2>
    <div class="slot"><div class="time">9.30 – 10.15</div>
      <p>Helen Marsh: Immediate past president of<br>the ADTA will be updating us on all things ECPD</p></div>
    <div class="slot"><div class="time">10.15 – 11.00</div>
      <p>Laura Benning: Will provide an update on teeth whiteing and explain how social media has impacted her business</p>
      <p>Claire Dunmore: Our internationally acclaimed speaker will update our knowledge of periodontal disease and nutrition and new technologies.</p></div>
    <div class="slot"><div class="time">11.00 – 11.30&nbsp; Break</div></div>
    <div class="slot"><div class="time">11.30 – 13.00</div>
      <p>Niamh Carroway &amp; Rachel Tindall: Will be providing a combined presentation on 'Scaling your business' and start to finish Sonaflow techniques. The aim being to build our business with effective communications, systems and protocols. This sessions promises audience participation!</p></div>
    <div class="slot"><div class="time">12.00 – 14.00 lunch</div></div>
    <div class="slot"><div class="time">14.00 – 15.00</div>
      <p>Sam Varley: Save your back. All things posture.</p></div>
    <div class="slot"><div class="time">15.00 – 15.30 Break</div></div>
    <div class="slot"><div class="time">15.30 – 16.30</div>
      <p>Claire Dunmore: Our internationally acclaimed speaker will update our knowledge of periodontal disease and nutrition and new technologies.</p></div>
  </section>

  <aside class="details">
    <address class="venue" style="font-style:normal">Larkfield Hotel<br>Meteor Road<br>Welbury<br>WB4 7QN</address>
    <div class="date">Friday 19<br>January 2018<br><span class="hours">09:00 – 16:30 GMT</span></div>
    <svg class="ticket-art" viewBox="0 0 116 92" role="img" aria-label="Illustration of a golden admission ticket">
      <rect x="14" y="22" width="88" height="48" rx="6" fill="var(--orange)" transform="rotate(-22 58 46)"/>
    </svg>
    <div class="booking">https://www.ticketdesk.example/e/fundraising-study-day-east-of-england-lift-the-january-blues-tickets-48210937716</div>
  </aside>
</main>
</body>
</html>
```